BRASKETT LAND SERVICES BILLBOARD DESIGN

I NEED A BILLBOARD FOR MY BUSINESS. WE ARE A LAND CLEARING COMPANY AND I WOULD LIKE TO ADD A PICTURE OF MY TRACK LOADER TO THE SIGN. OPEN TO COLORS. I WOULD ALSO LIKE TO HAVE MY PHONE NUMBER 555-284-7196, WEBSITE WWW.BRASKETTLANDSERVICES.EXAMPLE, AND EMAIL ON THE SIGN (CONTACT@BRASKETTLANDSERVICES.EXAMPLE). DESIGNERS CAN HAVE THE FREEDOM TO DO WHATEVER STYLE THEY WANT AND TO USE ANY COLORS THEY WANT.

Target Market(s)

ANYONE WITH PROPERTY

Requirements
Must have
• PICTURE OF TRACK LOADER, WEBSITE, PHONE NUMBER, EMAIL
Nice to have
• OPEN TO ANYTHING
Should not have
• OPEN TO ANYTHING

```html
<!DOCTYPE html>
<html lang="en">
<head>
<meta charset="utf-8">
<title>Braskett Land Services Billboard</title>
<link rel="stylesheet" href="https://fonts.googleapis.com/css2?family=Oswald:wght@500;600;700&display=swap">
<style>
  :root {
    --crimson: #a3132b;
    --ink: #151515;
    --paper: #ffffff;
    --backdrop: #e9ebee;
    --grass: #8a7a4e;
    --forest: #3f4a26;
    --loader: #e8552a;
  }
  * { margin: 0; padding: 0; box-sizing: border-box; }
  html, body {
    width: 1200px; height: 1200px; overflow: hidden;
    background: var(--backdrop);
  }
  .billboard {
    position: absolute;
    left: 40px; top: 385px;
    width: 1120px; height: 430px;
    background: var(--paper);
    box-shadow: 0 6px 24px rgba(0,0,0,.18);
    overflow: hidden;
    font-family: "Oswald", "Arial Narrow", sans-serif;
  }
  .photo-area {
    position: absolute; inset: 0;
    width: 1120px; height: 430px;
  }
  .brand {
    position: absolute; left: 32px; top: 0; bottom: 0;
    width: 440px;
    display: flex; flex-direction: column; justify-content: center;
  }
  .brand-name {
    color: var(--crimson);
    font-weight: 700;
    font-size: 62px;
    line-height: 0.98;
    text-transform: uppercase;
    white-space: nowrap;
  }
  .brand-rule {
    margin-top: 14px;
    width: 390px; height: 2px;
    background: var(--ink);
  }
  .phone {
    display: flex; align-items: center; gap: 12px;
    margin-top: 20px;
    color: var(--crimson);
    font-weight: 700;
    font-size: 58px;
    line-height: 1;
    white-space: nowrap;
  }
  .phone svg { width: 42px; height: 42px; flex: none; }
  .contact-line {
    display: flex; align-items: center; gap: 10px;
    margin-top: 14px;
    color: var(--ink);
    font-weight: 600;
    font-size: 20px;
    line-height: 1;
    white-space: nowrap;
  }
  .contact-line svg { width: 18px; height: 18px; flex: none; }
</style>
</head>
<body>
  <section class="billboard">
    <svg class="photo-area" viewBox="0 0 1120 430" role="img" aria-label="Photo of an orange compact track loader with a forestry mulcher head on a grassy clearing in front of trees">
      <defs>
        <linearGradient id="scene-tone" x1="0" y1="0" x2="0" y2="1">
          <stop offset="0" stop-color="var(--forest)"/>
          <stop offset="0.55" stop-color="#5a5a34"/>
          <stop offset="1" stop-color="var(--grass)"/>
        </linearGradient>
        <radialGradient id="machine-tone" cx="0.62" cy="0.5" r="0.45">
          <stop offset="0" stop-color="var(--loader)" stop-opacity="0.55"/>
          <stop offset="1" stop-color="var(--loader)" stop-opacity="0"/>
        </radialGradient>
      </defs>
      <path d="M520 0 Q450 215 520 430 L1120 430 L1120 0 Z" fill="url(#scene-tone)"/>
      <path d="M520 0 Q450 215 520 430 L1120 430 L1120 0 Z" fill="url(#machine-tone)"/>
      <path d="M520 0 Q450 215 520 430" fill="none" stroke="var(--crimson)" stroke-width="12"/>
    </svg>

    <div class="brand">
      <h1 class="brand-name">Braskett<br>Land Services</h1>
      <div class="brand-rule"></div>

      <p class="phone">
        <svg viewBox="0 0 24 24" aria-hidden="true">
          <path fill="var(--crimson)" d="M6.6 10.8a15.1 15.1 0 0 0 6.6 6.6l2.2-2.2a1 1 0 0 1 1-.25 11.4 11.4 0 0 0 3.6.57 1 1 0 0 1 1 1V20a1 1 0 0 1-1 1A17 17 0 0 1 3 4a1 1 0 0 1 1-1h3.5a1 1 0 0 1 1 1c0 1.25.2 2.45.57 3.57a1 1 0 0 1-.25 1z"/>
          <path fill="none" stroke="var(--crimson)" stroke-width="1.6" stroke-linecap="round" d="M14 3.5a7 7 0 0 1 6.5 6.5M14 7a3.6 3.6 0 0 1 3 3"/>
        </svg>
        555-284-7196
      </p>

      <p class="contact-line">
        <svg viewBox="0 0 24 24" aria-hidden="true">
          <g fill="none" stroke="var(--crimson)" stroke-width="1.8">
            <circle cx="12" cy="12" r="9.5"/>
            <ellipse cx="12" cy="12" rx="4.2" ry="9.5"/>
            <path d="M2.5 12h19M4 7h16M4 17h16"/>
          </g>
        </svg>
        WWW.BRASKETTLANDSERVICES.EXAMPLE
      </p>

      <p class="contact-line">
        <svg viewBox="0 0 24 24" aria-hidden="true">
          <rect x="2.5" y="5" width="19" height="14" rx="1.5" fill="var(--crimson)"/>
          <path d="M3 6l9 7 9-7" fill="none" stroke="var(--paper)" stroke-width="1.6"/>
        </svg>
        CONTACT@BRASKETTLANDSERVICES.EXAMPLE
      </p>
    </div>
  </section>
</body>
</html>
```